Truck Drivers Using App w/Jobsite Checklist

Looking for an 8" x 11" flyer that conveys to our customers (roofing contractors) that our drivers have tablets in each truck that have an app with a jobsite checklist that gives contractors less real time notifications and mistakes are caught with photos.
Should read something like this:
Ever wonder if your material has been delivered? We've got a solution for that!
All Trucks are equipped with dash-mounted tablet.
Here's what you get access to:
- Real Time Email Confirmation of Delivery
- Photos of Material Placement
- Before/After Photo of Driveway
- Material List of Products Delivered
- Homeowner Sign Off
Maybe a collage of the different photos available.
Target Market(s)
Roofing/Building Contractors
Industry/Entity Type
Roofing
Requirements
Must have
- website: www.harborfinchdepot.com
- tagline: Building Relationships, Building Trust - a Tradition Since 1905
- Photoshop format for further editing
Nice to have
- A smooth look to it.
- A collage of the photos avail on app

```html
<!DOCTYPE html>
<html lang="en">
<head>
<meta charset="utf-8">
<title>Harbor Finch Depot – Delivery Checklist Flyer</title>
<link href="https://fonts.googleapis.com/css2?family=Montserrat:wght@400;500;600;700;800&display=swap" rel="stylesheet">
<style>
  :root {
    --navy: #1b2a78;
    --ink: #111111;
    --list-ink: #121a4c;
    --cyan: #17b2e6;
    --periwinkle: #5b6fe0;
    --paper: #f1f2f4;
    --band: #1d1d20;
    --footer: #0f1a55;
    --white: #ffffff;
    --ring: #d9dbe0;
  }
  * { margin: 0; padding: 0; box-sizing: border-box; }
  html, body { width: 950px; height: 1200px; overflow: hidden; background: var(--paper); }
  body { font-family: "Montserrat", sans-serif; }
  .flyer { position: relative; width: 950px; height: 1200px; background: var(--paper); overflow: hidden; }
  .top-rule { position: absolute; left: 0; top: 0; width: 100%; height: 10px; background: #3a3a3c; }
  .brand { position: absolute; left: 44px; top: 80px; display: flex; align-items: center; gap: 12px; }
  .brand-dot { width: 34px; height: 34px; border-radius: 50%; background: var(--navy); }
  .brand-name { font-weight: 700; font-size: 24px; color: var(--navy); letter-spacing: 0.5px; line-height: 1.1; }
  .tagline { position: absolute; left: 46px; top: 196px; }
  .tagline span { display: block; font-weight: 700; line-height: 1; }
  .tag-big { font-size: 62px; color: var(--navy); letter-spacing: 1px; }
  .tag-small { font-size: 35px; color: var(--ink); letter-spacing: 0.5px; margin: 6px 0 8px; }
  .since { position: absolute; left: 47px; top: 404px; font-size: 21px; font-weight: 400; color: #222; letter-spacing: 0.5px; }
  .since-rule { position: absolute; left: 47px; top: 436px; width: 104px; height: 3px; background: var(--periwinkle); }
  .dark-band { position: absolute; left: 0; top: 469px; width: 100%; height: 293px; background: var(--band); }
  .collage { position: absolute; left: 0; top: 0; }
  .pitch { position: absolute; left: 46px; top: 482px; color: var(--white); font-weight: 600; font-size: 45px; line-height: 48px; }
  .pitch .accent { color: var(--cyan); }
  .pitch-note { position: absolute; left: 46px; top: 728px; color: var(--white); font-size: 18px; font-weight: 500; }
  .access-title { position: absolute; left: 46px; top: 778px; font-size: 37px; font-weight: 600; color: var(--ink); }
  .access-title .accent { color: var(--periwinkle); }
  .perks { position: absolute; left: 46px; top: 842px; list-style: none; }
  .perks li { display: flex; align-items: center; gap: 14px; height: 47.3px; font-size: 23px; font-weight: 600; color: var(--list-ink); }
  .perks svg { flex: none; }
  .contractor-photo { position: absolute; left: 704px; top: 657px; width: 236px; height: 434px; border-radius: 118px 118px 0 0; background: linear-gradient(180deg, #c89a78 0%, #7c9bbf 45%, #d7e43a 75%, #e8ebef 100%); }
  .footer-rule { position: absolute; left: 0; top: 1090px; width: 100%; height: 4px; background: var(--cyan); }
  .footer { position: absolute; left: 0; top: 1094px; width: 100%; height: 106px; background: linear-gradient(180deg, #1a2770, var(--footer)); text-align: center; }
  .footer-lead { margin-top: 12px; font-size: 24px; font-weight: 400; color: var(--cyan); }
  .footer-url { margin-top: 6px; display: inline-flex; align-items: center; gap: 14px; font-size: 34px; font-weight: 700; color: var(--white); }
</style>
</head>
<body>
<main class="flyer">
  <div class="top-rule"></div>

  <div class="brand">
    <div class="brand-dot"></div>
    <div class="brand-name">HARBOR FINCH<br>DEPOT</div>
  </div>

  <h1 class="tagline">
    <span class="tag-big">BUILDING</span>
    <span class="tag-small">RELATIONSHIPS</span>
    <span class="tag-big">BUILDING</span>
    <span class="tag-small">TRUST</span>
  </h1>
  <p class="since">A TRADITION SINCE 1905</p>
  <div class="since-rule"></div>

  <div class="dark-band"></div>

  <svg class="collage" width="950" height="720" viewBox="0 0 950 720">
    <defs>
      <linearGradient id="roofGrad" x1="0" y1="0" x2="0" y2="1">
        <stop offset="0" stop-color="#b9cde6"/>
        <stop offset="0.5" stop-color="#6e7fa8"/>
        <stop offset="1" stop-color="#a08a78"/>
      </linearGradient>
      <linearGradient id="palletGrad" x1="0" y1="0" x2="0" y2="1">
        <stop offset="0" stop-color="#8a9a86"/>
        <stop offset="1" stop-color="#3c4150"/>
      </linearGradient>
      <linearGradient id="truckGrad" x1="0" y1="0" x2="0" y2="1">
        <stop offset="0" stop-color="#7fb2e0"/>
        <stop offset="0.6" stop-color="#e4e7ec"/>
        <stop offset="1" stop-color="#5a5f66"/>
      </linearGradient>
      <linearGradient id="dashGrad" x1="0" y1="0" x2="0" y2="1">
        <stop offset="0" stop-color="#e9ecef"/>
        <stop offset="0.55" stop-color="#b7bcc3"/>
        <stop offset="1" stop-color="#2b2d31"/>
      </linearGradient>
    </defs>
    <circle cx="860" cy="270" r="395" fill="var(--ring)"/>
    <circle cx="860" cy="270" r="385" fill="url(#roofGrad)" role="img" aria-label="Roofers in safety harnesses laying shingles on a roof"/>
    <circle cx="488" cy="151" r="86" fill="var(--white)" stroke="#9a9ca2" stroke-width="2"/>
    <circle cx="488" cy="151" r="78" fill="url(#palletGrad)" role="img" aria-label="Bundles of shingles stacked on a roof deck"/>
    <circle cx="516" cy="388" r="107" fill="var(--white)" stroke="#9a9ca2" stroke-width="2"/>
    <circle cx="516" cy="388" r="98" fill="url(#truckGrad)" role="img" aria-label="Delivery flatbed truck with boom loader carrying roofing material"/>
    <circle cx="785" cy="496" r="130" fill="var(--white)" stroke="#9a9ca2" stroke-width="2"/>
    <circle cx="785" cy="496" r="120" fill="url(#dashGrad)" role="img" aria-label="Truck cab with a dash-mounted tablet showing the jobsite checklist"/>
  </svg>

  <h2 class="pitch">Ever wonder<br>if your material has<br>been delivered?<br><span class="accent">We've got a solution<br>for that!</span></h2>
  <p class="pitch-note">All Trucks are equipped with dash-mounted tablet.</p>

  <div class="contractor-photo" role="img" aria-label="Smiling site supervisor in a high-visibility vest holding a tablet"></div>

  <h3 class="access-title">Here's what you <span class="accent">get access to</span></h3>
  <ul class="perks">
    <li><svg width="20" height="20" viewBox="0 0 20 20"><circle cx="10" cy="10" r="9.5" fill="#e3e4e8"/><path d="M8 5.5 L12.5 10 L8 14.5" fill="none" stroke="#111" stroke-width="2.4"/></svg>Real Time Email Confirmation of Delivery</li>
    <li><svg width="20" height="20" viewBox="0 0 20 20"><circle cx="10" cy="10" r="9.5" fill="#e3e4e8"/><path d="M8 5.5 L12.5 10 L8 14.5" fill="none" stroke="#111" stroke-width="2.4"/></svg>Photos of Material Placement</li>
    <li><svg width="20" height="20" viewBox="0 0 20 20"><circle cx="10" cy="10" r="9.5" fill="#e3e4e8"/><path d="M8 5.5 L12.5 10 L8 14.5" fill="none" stroke="#111" stroke-width="2.4"/></svg>Before/After Photo of Driveway</li>
    <li><svg width="20" height="20" viewBox="0 0 20 20"><circle cx="10" cy="10" r="9.5" fill="#e3e4e8"/><path d="M8 5.5 L12.5 10 L8 14.5" fill="none" stroke="#111" stroke-width="2.4"/></svg>Material List of Products Delivered</li>
    <li><svg width="20" height="20" viewBox="0 0 20 20"><circle cx="10" cy="10" r="9.5" fill="#e3e4e8"/><path d="M8 5.5 L12.5 10 L8 14.5" fill="none" stroke="#111" stroke-width="2.4"/></svg>Homeowner Sign Off</li>
  </ul>

  <div class="footer-rule"></div>
  <footer class="footer">
    <p class="footer-lead">Contact us for an obligation free quote:</p>
    <p class="footer-url">
      <svg width="26" height="26" viewBox="0 0 26 26" fill="none" stroke="#2fb7e8" stroke-width="1.8">
        <circle cx="13" cy="13" r="11"/><ellipse cx="13" cy="13" rx="5" ry="11"/><path d="M2 13 H24 M4 7 H22 M4 19 H22"/>
      </svg>
      WWW.HARBORFINCHDEPOT.COM
    </p>
  </footer>
</main>
</body>
</html>
```